Mosk trail Website

We need a simple web page design for our businessWe procure and dispose of earthmoving construction equipmentwe also find construction equipment for our customers using our global contacts

Number of Pages Required

1 page

```html
<!DOCTYPE html>
<html lang="en">
<head>
<meta charset="utf-8">
<title>Mosk trail</title>
<link href="https://fonts.googleapis.com/css2?family=Poppins:wght@500;600;700;800&family=Open+Sans:wght@400;600;700&display=swap" rel="stylesheet">
<style>
:root{
  --yellow:#f7b90f;
  --dark:#1b1b1b;
  --text:#2b2b2b;
  --muted:#4a4a4a;
  --light:#f3f1f0;
  --sky:#a9c4ea;
  --ground:#2a2a2a;
  --footer:#262626;
  --white:#ffffff;
}
*{margin:0;padding:0;box-sizing:border-box}
html,body{width:1200px;height:3863px;overflow:hidden}
body{font-family:"Open Sans",sans-serif;color:var(--text);background:var(--white);position:relative}
section,header,footer{position:absolute;left:0;width:1200px}
.abs{position:absolute}
.btn{position:absolute;display:flex;align-items:center;justify-content:center;gap:10px;background:var(--yellow);color:var(--dark);font-family:"Poppins",sans-serif;font-weight:700;font-size:15px;letter-spacing:.5px;height:42px;padding:0 24px;box-shadow:0 3px 6px rgba(0,0,0,.15);white-space:nowrap}
.btn svg{width:12px;height:12px}
h2,h3,h4{font-family:"Poppins",sans-serif;color:var(--dark)}
.dot{color:var(--yellow)}

/* hero */
.hero{top:0;height:664px;background:linear-gradient(180deg,#6b5a52 0%,#8a6a58 30%,#7d5e4a 55%,#5a4436 100%)}
.hero-photo{position:absolute;inset:0;background:radial-gradient(ellipse at 45% 40%,rgba(214,170,60,.45) 0,rgba(0,0,0,0) 35%),linear-gradient(180deg,rgba(40,40,60,.25),rgba(30,20,15,.35))}
.brand{font-family:"Poppins",sans-serif;font-weight:700;color:var(--white);font-size:28px;letter-spacing:.5px}
.nav{position:absolute;top:30px;left:559px;display:flex;gap:24px;font-family:"Poppins",sans-serif;font-weight:600;font-size:13px;color:var(--white)}
.nav .active{color:var(--yellow);border-bottom:3px solid var(--yellow);padding-bottom:4px}
.search{position:absolute;top:20px;left:1026px;width:30px;height:30px;border:2px solid var(--white);border-radius:50%}
.hero h1{position:absolute;left:817px;top:190px;font-family:"Poppins",sans-serif;font-weight:700;color:var(--white);font-size:58px;line-height:60px}
.hero p{position:absolute;left:820px;top:326px;width:330px;color:var(--white);font-weight:700;font-size:20px;line-height:25px}
.dots{position:absolute;top:594px;left:546px;display:flex;gap:14px;align-items:center}
.dots span{width:10px;height:10px;border-radius:50%;background:var(--white)}
.dots span.on{width:14px;height:14px;background:none;border:2px solid var(--white)}

/* features */
.features{top:664px;height:336px}
.feature{position:absolute;top:60px;width:280px}
.feature svg{width:86px;height:86px}
.feature h3{margin-top:26px;font-size:16px;line-height:22px;font-weight:700}
.feature p{margin-top:10px;font-size:13px;line-height:17px;color:var(--muted)}
.divider{position:absolute;top:48px;width:1px;height:230px;background:#ddd}

/* welcome */
.welcome{top:1000px;height:571px;background:var(--light)}
.welcome .eyebrow{position:absolute;left:144px;top:112px;font-family:"Poppins",sans-serif;font-weight:600;font-size:18px}
.welcome .rule{position:absolute;left:0;top:148px;width:104px;height:3px;background:#c8c6c5}
.welcome h2{position:absolute;left:144px;top:135px;font-size:52px;font-weight:700;letter-spacing:1px}
.welcome p{position:absolute;left:144px;top:228px;width:370px;font-size:14.5px;line-height:20px;color:var(--muted)}
.welcome-photo{position:absolute;left:577px;top:43px;width:623px;height:484px;background:radial-gradient(circle at 48% 52%,#ffd65a 0,#f1a01a 9%,#b85a0c 26%,#3a1c08 55%,#100804 80%)}

/* services */
.services{top:1648px;height:721px}
.services-photo{position:absolute;left:0;top:0;width:572px;height:721px;background:linear-gradient(180deg,#a7b3c2 0%,#c6ccd2 35%,#b39a6c 55%,#8a7350 100%)}
.services .eyebrow{position:absolute;left:641px;top:12px;font-family:"Poppins",sans-serif;font-weight:700;font-size:17px}
.services .eyebrow::after{content:"";display:block;width:40px;height:3px;background:var(--yellow);margin-top:8px}
.service{position:absolute;left:641px;width:390px}
.service h3{font-size:26px;font-weight:700}
.service p{margin-top:8px;font-size:12.5px;line-height:16px;color:var(--muted)}
.link-line{position:absolute;left:572px;width:92px;height:1px;background:#555}

/* procurement */
.procure{top:2438px;height:593px}
.procure-photo{position:absolute;left:440px;top:0;width:760px;height:593px;background:linear-gradient(180deg,#3a72c4 0%,#7fa9df 40%,#c9d7e8 62%,#9c7c55 82%,#6c5238 100%)}
.procure-card{position:absolute;left:142px;top:98px;width:507px;height:412px;background:var(--white);box-shadow:0 6px 24px rgba(0,0,0,.25)}
.procure-card h2{position:absolute;left:60px;top:52px;width:400px;font-size:23px;line-height:27px;font-weight:700}
.procure-card p{position:absolute;left:60px;top:176px;width:360px;font-size:15px;line-height:20px;color:var(--muted)}

/* cta */
.cta{top:3090px;height:458px;background:var(--sky)}
.cta h2{position:absolute;left:0;width:1200px;top:92px;text-align:center;font-size:25px;line-height:34px;font-weight:700}
.cta-scene{position:absolute;left:0;top:268px;width:1200px;height:150px;background:linear-gradient(180deg,var(--sky) 0%,#b3cbec 100%)}
.cta-ground{position:absolute;left:0;top:418px;width:1200px;height:40px;background:var(--ground)}

/* footer */
.footer{top:3548px;height:315px;background:var(--footer);color:#e6e6e6}
.footer .brand{position:absolute;left:142px;top:98px;font-size:30px}
.fcol{position:absolute;top:40px;font-size:11.5px}
.fcol h4{color:var(--white);font-size:12.5px;font-weight:600;margin-bottom:18px;letter-spacing:.4px}
.fcol li{list-style:none;line-height:16px}
.contact-row{display:flex;gap:14px;margin-bottom:16px;line-height:15px}
.contact-row svg{width:12px;height:12px;flex:none;margin-top:2px}
.social li{display:flex;align-items:center;gap:12px;margin-bottom:12px}
.social .circ{width:26px;height:26px;border-radius:50%;background:#3b5fa8}
.copyright{position:absolute;left:0;width:1200px;top:276px;text-align:center;font-size:11.5px;color:#ddd}
</style>
</head>
<body>

<header class="hero">
  <div class="hero-photo" role="img" aria-label="Yellow excavator on a dusty construction site under a dramatic sky"></div>
  <div class="brand abs" style="left:144px;top:24px">MOSK TRAIL</div>
  <nav class="nav"><span class="active">HOME</span><span>ABOUT US</span><span>SERVICES</span><span>BLOG</span><span>PARTS</span><span>CONTACT US</span></nav>
  <div class="search"><svg viewBox="0 0 26 26" width="26" height="26"><circle cx="12" cy="12" r="4.5" fill="none" stroke="#fff" stroke-width="2"/><line x1="15.5" y1="15.5" x2="19" y2="19" stroke="#fff" stroke-width="2"/></svg></div>
  <h1>Service<br>On Earth<span class="dot">.</span></h1>
  <p>Lorem Ipsum is simply dummy text of the printing and type setting industry</p>
  <a class="btn" style="left:824px;top:432px;height:48px">READ MORE <svg viewBox="0 0 12 12"><path d="M2 2l4 4-4 4M6 2l4 4-4 4" fill="none" stroke="#1b1b1b" stroke-width="1.8"/></svg></a>
  <div class="dots"><span></span><span></span><span class="on"></span><span></span><span></span></div>
</header>

<section class="features">
  <div class="feature" style="left:144px">
    <svg viewBox="0 0 86 86"><path d="M8 76h40M14 76V58h16v18M22 58l36-40 20 10M30 58l28-40M58 18v22M70 26v14" fill="none" stroke="#f7b90f" stroke-width="4"/><circle cx="70" cy="46" r="5" fill="#f7b90f"/></svg>
    <h3>CONSTRUCTION<br>EQUIPMENT SERVICES</h3>
    <p>Lorem ipsum dolor sit amet consectetur adipiscing elit sed do eiusmod tempor incididunt ut labore.</p>
  </div>
  <div class="divider" style="left:420px"></div>
  <div class="feature" style="left:477px">
    <svg viewBox="0 0 86 86"><path d="M30 40h8l8-14c4 0 5 4 4 8l-2 6h12c4 0 5 4 3 6l-3 16c-1 3-3 4-6 4H38V40z" fill="#f7b90f"/><rect x="24" y="40" width="10" height="26" fill="#f7b90f"/><g fill="#f7b90f"><circle cx="43" cy="10" r="3"/><circle cx="20" cy="18" r="3"/><circle cx="66" cy="18" r="3"/><circle cx="10" cy="42" r="3"/><circle cx="76" cy="42" r="3"/><circle cx="18" cy="70" r="3"/><circle cx="68" cy="72" r="3"/></g></svg>
    <h3>YOU WANT QUALITY<br>WE PROMISE!</h3>
    <p>Lorem ipsum dolor sit amet consectetur adipiscing elit sed do eiusmod tempor incididunt ut labore.</p>
  </div>
  <div class="divider" style="left:763px"></div>
  <div class="feature" style="left:818px">
    <svg viewBox="0 0 86 86"><circle cx="34" cy="50" r="16" fill="none" stroke="#f7b90f" stroke-width="9" stroke-dasharray="6 4"/><circle cx="34" cy="50" r="7" fill="#f7b90f"/><circle cx="60" cy="24" r="11" fill="none" stroke="#f7b90f" stroke-width="7" stroke-dasharray="5 3"/><circle cx="60" cy="24" r="4" fill="#f7b90f"/></svg>
    <h3>REFURBISHMENT SERVICE<br>FOR PLANT AND EQUIPMENT</h3>
    <p>Lorem ipsum dolor sit amet consectetur adipiscing elit sed do eiusmod tempor incididunt ut labore.</p>
  </div>
</section>

<section class="welcome">
  <div class="rule"></div>
  <div class="eyebrow">WELCOME TO OUR SITE</div>
  <h2>MOSK TRAIL</h2>
  <p>But I must explain to you how all this mistaken idea of denouncing pleasure and praising pain was born and I will give you a complete account of the system, and expound the actual teachings of the great explorer of the truth, the master-builder of human happiness. No one rejects, dislikes, or avoids pleasure itself, because it is pleasure, but because those who do not know how to pursue pleasure rationally encounter.</p>
  <a class="btn" style="left:146px;top:424px;height:40px">READ MORE <svg viewBox="0 0 12 12"><path d="M2 2l4 4-4 4M6 2l4 4-4 4" fill="none" stroke="#1b1b1b" stroke-width="1.8"/></svg></a>
  <div class="welcome-photo" role="img" aria-label="Excavator silhouetted against a glowing sunset"></div>
</section>

<section class="services">
  <div class="services-photo" role="img" aria-label="Yellow wheel loader with a large bucket on a gravel site"></div>
  <div class="eyebrow">OUR SERVICES</div>
  <div class="link-line" style="top:188px"></div>
  <div class="link-line" style="top:322px"></div>
  <div class="link-line" style="top:494px"></div>
  <div class="service" style="top:68px"><h3>Bucket Rebuilds &amp; Repairs<span class="dot">.</span></h3><p>But I must explain to you how all this mistaken idea of denouncing pleasure and praising pain was born and I will give you a complete</p></div>
  <div class="service" style="top:204px"><h3>Engine Reconditioning<span class="dot">.</span></h3><p>At vero eos et accusamus et iusto odio dignissimos ducimus qui blanditiis praesentium voluptatum deleniti atque corrupti quos dolores et quas molestias.</p></div>
  <div class="service" style="top:346px"><h3>Supply &amp; Reuse<span class="dot">.</span></h3><p>On the other hand, we denounce with righteous indignation and dislike men who are so beguiled and demoralized by the charms of pleasure of the moment, so blinded by desire, that they cannot foresee the pain and trouble that are bound to ensue; and equal blame belongs to those who fail.</p></div>
  <div class="service" style="top:516px"><h3>Material Disposal<span class="dot">.</span></h3><p>Minus id quod maxime placeat facere possimus, omnis voluptas assumenda est, omnis dolor repellendus. Temporibus autem quibusdam et aut officiis debitis.</p></div>
  <a class="btn" style="left:644px;top:650px;height:40px">READ MORE <svg viewBox="0 0 12 12"><path d="M2 2l4 4-4 4M6 2l4 4-4 4" fill="none" stroke="#1b1b1b" stroke-width="1.8"/></svg></a>
</section>

<section class="procure">
  <div class="procure-photo" role="img" aria-label="Wheel loader raising its bucket against a blue sky with clouds"></div>
  <div class="procure-card">
    <h2>PROCUREMENT AND DISPOSAL MANAGEMENT FOR THE EARTHMOVING CONSTRUCTION EQUIPMENT.</h2>
    <p>On the other hand, we denounce with righteous indignation and dislike men who are so beguiled and demoralized by the charms of pleasure of the moment, so blinded by desire, that they cannot foresee the pain and trouble that</p>
    <a class="btn" style="left:64px;top:322px;height:40px">READ MORE <svg viewBox="0 0 12 12"><path d="M2 2l4 4-4 4M6 2l4 4-4 4" fill="none" stroke="#1b1b1b" stroke-width="1.8"/></svg></a>
  </div>
</section>

<section class="cta">
  <h2>LOREM IPSUM IS SIMPLY DUMMY TEXT OF<br>THE PRINTING AND TYPESETTING.</h2>
  <a class="btn" style="left:520px;top:201px;width:162px;height:44px">CONTACT US</a>
  <div class="cta-scene" role="img" aria-label="Flat illustration of clouds, small construction vehicles and a building along the ground"></div>
  <div class="cta-ground"></div>
</section>

<footer class="footer">
  <div class="brand">MOSK TRAIL</div>
  <div class="fcol" style="left:438px">
    <h4>CONTACT US</h4>
    <div class="contact-row"><svg viewBox="0 0 12 12"><path d="M6 11S2 6.8 2 4.5a4 4 0 018 0C10 6.8 6 11 6 11z" fill="#ddd"/><circle cx="6" cy="4.5" r="1.4" fill="#262626"/></svg><div>Keldermolen 24<br>4410 RB Veldhaven, The Netherlands</div></div>
    <div class="contact-row"><svg viewBox="0 0 12 12"><path d="M3 1l2 2.5-1.2 1.5a7 7 0 003.2 3.2L8.5 7 11 9l-1.5 2C5 11 1 7 1 2.5z" fill="#ddd"/></svg><div>055.555.0142</div></div>
    <div class="contact-row"><svg viewBox="0 0 12 12"><rect x="1" y="2.5" width="10" height="7" fill="#ddd"/><path d="M1 2.5l5 4 5-4" fill="none" stroke="#262626" stroke-width="1"/></svg><div>info@mosktrail.com</div></div>
  </div>
  <div class="fcol" style="left:736px">
    <h4>MENU</h4>
    <ul><li>Home</li><li>About Us</li><li>Services</li><li>Blog</li><li>Testimonials</li><li>Contact Us</li></ul>
  </div>
  <div class="fcol" style="left:932px">
    <h4>CONNECT WITH US</h4>
    <ul class="social"><li><span class="circ"></span>Facepage</li><li><span class="circ" style="background:#2aa6e0"></span>Chirper</li><li><span class="circ" style="background:#1e4f86"></span>Linkwork</li></ul>
  </div>
  <div class="copyright">Copyrights @ 2018 All Rights Reserved</div>
</footer>

</body>
</html>
```